Healthcare IT company looking for business card design

We develop IT systems for healthcare that significantly reduces cost and improves quality.

We want a business card design that is professional and clean, and using the colors in our logo.

Target Market(s)

Doctors and decision makers in the healthcare industry

Industry/Entity Type

Healthcare

Contact Information for Business Card

It should include
Name and title, address, telephone

Tobias Vrenholt, CEO
+46 712 418257
tobias@kelvaro.se

Font styles to use
Serif

Colors
0355a3
ed282f

Requirements
Must have
• Clean design
• Professional feel
Nice to have
• N/A
Should not have
• N/A

```html
<!DOCTYPE html>
<html lang="en">
<head>
<meta charset="utf-8">
<title>Tobias Vrenholt – Kelvaro business card</title>
<link rel="stylesheet" href="https://fonts.googleapis.com/css2?family=Jost:wght@400;500&display=swap">
<style>
  :root {
    --card-bg: #ffffff;
    --ink: #111111;
    --brand-red: #ed282f;
    --brand-blue: #0355a3;
  }
  * { margin: 0; padding: 0; box-sizing: border-box; }
  html, body {
    width: 1200px;
    height: 686px;
    overflow: hidden;
    background: var(--card-bg);
  }
  .card {
    position: relative;
    width: 1200px;
    height: 686px;
    background: var(--card-bg);
    font-family: "Jost", "Futura", sans-serif;
    color: var(--ink);
  }
  .contact {
    position: absolute;
    left: 0;
    right: 0;
    text-align: center;
    line-height: 1;
    white-space: nowrap;
    font-weight: 400;
  }
  .contact__name {
    top: 232px;
    font-size: 56px;
    letter-spacing: 0.12em;
  }
  .contact__rule {
    position: absolute;
    left: 448px;
    top: 320px;
    width: 304px;
    height: 5px;
    background: var(--brand-red);
  }
  .contact__phone {
    top: 358px;
    font-size: 51px;
    letter-spacing: 0.12em;
  }
  .contact__email {
    top: 414px;
    font-size: 50px;
    letter-spacing: 0.15em;
  }
  .brand {
    position: absolute;
    right: 48px;
    bottom: 44px;
    display: flex;
    align-items: center;
    gap: 16px;
  }
  .brand__dot {
    width: 36px;
    height: 36px;
    border-radius: 50%;
    background: var(--brand-blue);
  }
  .brand__name {
    font-family: "Jost", "Futura", sans-serif;
    font-size: 44px;
    font-weight: 500;
    letter-spacing: 0.06em;
    color: var(--brand-red);
    line-height: 1;
  }
</style>
</head>
<body>
  <main class="card">
    <h1 class="contact contact__name">Tobias Vrenholt // CEO</h1>
    <span class="contact__rule" aria-hidden="true"></span>
    <p class="contact contact__phone">+46 712 418257</p>
    <p class="contact contact__email">tobias@kelvaro.se</p>

    <div class="brand">
      <span class="brand__dot" aria-hidden="true"></span>
      <span class="brand__name">Kelvaro</span>
    </div>
  </main>
</body>
</html>
```